New Website for World Wide Charity (KELVOR)

We need a dynamic web design for our brand new charity organisation that will be working worldwide. We will be funded by donations so need to attract people to donate.

What We Do
We work to optimise the wellbeing of the planet, the animals and all that live within. Our slogan is Achieving Vibrational Equilibrium.

We have included a Powerpoint document which may help you understand what we need, it is just an idea for structure and style, it is not set in stone so feel free to be as creative as you like!
Updates

Designs look the same

Target Market(s)

Adults 18+ with an interest in animal, environmental. Businesses that may like to support our natural world or already support our natural world.

Number of Pages Required

3 page

Colors

Designer to choose colors to be used in the design.

Requirements
Must have
• We need the website to be easy to use and understand.

Web pages will be Home, What We Do, Who We Are, Success Stories, What You Can Do (Blog section), Seek Help, Donate, Join.
Nice to have
• Natural feel, easy to navigate, Ideally the website will look natural and organic.

Natural colours, blues, greens, sand, gold, brown, grey, silver, Orange and yellow for impact.
Should not have
• Should not have a dark coloured theme.

```html
<!DOCTYPE html>
<html lang="en">
<head>
<meta charset="utf-8">
<title>KELVOR – Achieving Vibrational Equilibrium</title>
<link href="https://fonts.googleapis.com/css2?family=Montserrat:wght@400;500;600&family=Open+Sans:wght@400&display=swap" rel="stylesheet">
<style>
:root{
  --nav-blue:#4f7fba;
  --deep-teal:#1f5a74;
  --navy:#0e3a54;
  --ink:#3a3a3a;
  --body-text:#5a5a5a;
  --sky-left:#b8f6fb;
  --sky-right:#dcecfc;
  --panel-mint:#eefaff;
  --panel-ice:#f2f7ff;
  --footer-blue:#4f82ba;
  --white:#ffffff;
  --link-blue:#4f7fba;
  --logo-lilac:#e6dcee;
}
html,body{margin:0;padding:0;overflow:hidden;}
body{width:1200px;height:3330px;font-family:"Open Sans",Arial,sans-serif;background:var(--white);}
.page{position:relative;width:1200px;height:3330px;overflow:hidden;background:var(--white);}

/* Hero */
.hero{position:absolute;left:0;top:0;width:1200px;height:890px;background:linear-gradient(90deg,var(--sky-left),var(--sky-right));}
.hero-scene{position:absolute;left:0;top:0;width:1200px;height:890px;}
.main-nav{position:absolute;left:111px;top:93px;width:978px;height:61px;background:var(--nav-blue);}
.main-nav a{position:absolute;top:0;line-height:61px;color:var(--white);font-family:"Montserrat",Arial,sans-serif;font-weight:500;font-size:14.5px;text-decoration:none;white-space:nowrap;}
.brand-badge{position:absolute;left:484px;top:17px;width:212px;height:212px;border-radius:50%;background:var(--white);}
.brand-badge .ring{position:absolute;left:12px;top:12px;width:182px;height:182px;border-radius:50%;border:3px solid var(--nav-blue);background:var(--logo-lilac);box-sizing:border-box;}
.brand-badge .name{position:absolute;left:0;top:0;width:212px;line-height:212px;text-align:center;font-family:"Montserrat",Arial,sans-serif;font-weight:500;font-size:30px;color:var(--deep-teal);letter-spacing:1px;}
.hero-title{position:absolute;left:0;top:254px;width:1200px;text-align:center;margin:0;font-family:"Montserrat",Arial,sans-serif;font-weight:500;font-size:31px;line-height:38px;color:var(--deep-teal);letter-spacing:.5px;}
.hero-sub{position:absolute;left:0;top:304px;width:1200px;text-align:center;margin:0;font-family:"Montserrat",Arial,sans-serif;font-weight:500;font-size:26px;line-height:34px;color:var(--ink);}
.cta{position:absolute;left:493px;top:353px;width:214px;height:59px;border-radius:30px;background:var(--navy);color:var(--white);text-align:center;line-height:59px;font-family:"Montserrat",Arial,sans-serif;font-weight:500;font-size:15.5px;text-decoration:none;}

/* Focus circles */
.focus{position:absolute;left:0;top:890px;width:1200px;height:510px;background:linear-gradient(180deg,#ffffff 0%,#f4f6f8 55%,#ffffff 100%);}
.focus-item{position:absolute;top:73px;width:244px;text-align:center;}
.focus-item .photo{width:244px;height:244px;border-radius:50%;}
.focus-item h3{margin:18px 0 0;font-family:"Montserrat",Arial,sans-serif;font-weight:500;font-size:22px;color:var(--ink);letter-spacing:.5px;}
.focus-item a{display:inline-block;margin-top:8px;font-family:"Montserrat",Arial,sans-serif;font-weight:600;font-size:12.5px;color:var(--link-blue);text-decoration:underline;}

/* Feature rows */
.feature{position:absolute;left:0;width:1200px;height:467px;}
.feature .photo{position:absolute;top:0;width:600px;height:467px;}
.feature .copy{position:absolute;top:0;width:600px;height:467px;}
.feature h2{position:absolute;left:59px;top:70px;margin:0;font-family:"Montserrat",Arial,sans-serif;font-weight:500;font-size:33px;color:var(--navy);letter-spacing:.5px;}
.feature p{position:absolute;left:62px;top:136px;width:412px;margin:0;font-size:14.6px;line-height:25.8px;color:var(--body-text);}
.read-more{position:absolute;left:64px;top:346px;width:159px;height:51px;border:2px solid var(--navy);border-radius:27px;text-align:center;line-height:51px;font-family:"Montserrat",Arial,sans-serif;font-weight:500;font-size:16px;color:var(--navy);text-decoration:none;}

/* Footer */
.footer-edge{position:absolute;left:0;top:2870px;width:1200px;height:70px;}
.site-footer{position:absolute;left:0;top:2935px;width:1200px;height:395px;background:var(--footer-blue);}
.footer-badge{position:absolute;left:159px;top:61px;width:214px;height:214px;border-radius:50%;background:var(--logo-lilac);}
.footer-badge .name{position:absolute;left:-30px;top:0;width:274px;line-height:214px;text-align:center;font-family:"Montserrat",Arial,sans-serif;font-weight:500;font-size:31px;color:var(--white);letter-spacing:1px;}
.footer-col{position:absolute;top:65px;}
.footer-col h4{margin:0 0 17px;font-family:"Montserrat",Arial,sans-serif;font-weight:500;font-size:21px;color:var(--white);}
.footer-col a{display:block;margin-left:2px;font-size:17px;line-height:38.8px;color:var(--white);text-decoration:none;}
.footer-rule{position:absolute;left:111px;top:319px;width:978px;height:1px;background:rgba(255,255,255,.3);}
.footer-meta{position:absolute;top:338px;margin:0;font-family:"Montserrat",Arial,sans-serif;font-size:15.5px;color:var(--white);}
</style>
</head>
<body>
<div class="page">

  <header class="hero">
    <svg class="hero-scene" viewBox="0 0 1200 890" role="img" aria-label="Illustrated rainforest hills in layered blues with a green bear silhouette and a person with arms raised">
      <defs>
        <linearGradient id="hillFar" x1="0" y1="0" x2="0" y2="1">
          <stop offset="0" stop-color="#a9d6f0"/>
          <stop offset="1" stop-color="#7fb6dc"/>
        </linearGradient>
        <linearGradient id="hillMid" x1="0" y1="0" x2="0" y2="1">
          <stop offset="0" stop-color="#6aa2c9"/>
          <stop offset="1" stop-color="#3f7aa6"/>
        </linearGradient>
        <linearGradient id="hillNear" x1="0" y1="0" x2="1" y2="0">
          <stop offset="0" stop-color="#2f6a7e"/>
          <stop offset="0.5" stop-color="#2c6190"/>
          <stop offset="1" stop-color="#1f5488"/>
        </linearGradient>
        <linearGradient id="hillFront" x1="0" y1="0" x2="1" y2="0">
          <stop offset="0" stop-color="#174d5e"/>
          <stop offset="0.6" stop-color="#153f66"/>
          <stop offset="1" stop-color="#0f3a68"/>
        </linearGradient>
        <radialGradient id="greenGlow" cx="0.5" cy="0.5" r="0.5">
          <stop offset="0" stop-color="#c8f0b8" stop-opacity=".95"/>
          <stop offset="0.55" stop-color="#78c47e" stop-opacity=".7"/>
          <stop offset="1" stop-color="#78c47e" stop-opacity="0"/>
        </radialGradient>
        <radialGradient id="paleGlow" cx="0.5" cy="0.5" r="0.5">
          <stop offset="0" stop-color="#d6e6f4" stop-opacity=".75"/>
          <stop offset="1" stop-color="#d6e6f4" stop-opacity="0"/>
        </radialGradient>
      </defs>
      <path d="M0 445 C80 420 150 430 220 440 C300 420 380 415 460 430 C540 412 600 420 660 440 C740 410 830 418 900 430 C980 405 1080 410 1200 440 L1200 890 L0 890 Z" fill="url(#hillFar)"/>
      <path d="M0 520 C90 495 180 500 260 515 C360 490 460 500 560 525 C660 500 760 505 860 520 C960 490 1080 495 1200 515 L1200 890 L0 890 Z" fill="url(#hillMid)"/>
      <path d="M0 610 C110 585 220 595 330 610 C440 590 560 600 680 615 C800 590 920 595 1040 605 C1100 598 1160 600 1200 608 L1200 890 L0 890 Z" fill="url(#hillNear)"/>
      <path d="M0 720 C140 700 280 710 420 725 C560 705 700 712 840 728 C960 712 1080 715 1200 722 L1200 890 L0 890 Z" fill="url(#hillFront)"/>
      <ellipse cx="500" cy="740" rx="210" ry="120" fill="url(#greenGlow)"/>
      <ellipse cx="900" cy="690" rx="170" ry="170" fill="url(#paleGlow)"/>
      <path d="M0 835 C40 826 80 822 120 818 C170 812 220 808 270 810 C310 830 330 860 360 872 C420 862 480 860 540 855 C620 850 700 848 780 848 C860 846 940 842 1020 836 C1090 832 1150 828 1200 826 L1200 890 L0 890 Z" fill="#ffffff"/>
    </svg>

    <nav class="main-nav">
      <a href="#" style="left:18px">HOME</a>
      <a href="#" style="left:94px">WHAT WE DO</a>
      <a href="#" style="left:224px">WHO WE ARE</a>
      <a href="#" style="left:601px">SUCCESS STORIES</a>
      <a href="#" style="left:762px">BLOG</a>
      <a href="#" style="left:832px">DONATE</a>
      <a href="#" style="left:924px">JOIN</a>
    </nav>

    <div class="brand-badge">
      <div class="ring"></div>
      <div class="name">KELVOR</div>
    </div>

    <h1 class="hero-title">HELP RAISE WORLD VIBRATION</h1>
    <p class="hero-sub">Achieving Vibrational Equilibrium</p>
    <a class="cta" href="#">MAKE A DIFFERENCE</a>
  </header>

  <section class="focus">
    <div class="focus-item" style="left:152px">
      <div class="photo" role="img" aria-label="Hands passing a seedling in soil" style="background:radial-gradient(circle at 40% 40%,#e8f2c8,#7fb84a 60%,#3f7a2a)"></div>
      <h3>ENVIRONMENT</h3>
      <a href="#">FIND OUT MORE &#187;</a>
    </div>
    <div class="focus-item" style="left:478px">
      <div class="photo" role="img" aria-label="Bear family among forest trees" style="background:radial-gradient(circle at 50% 50%,#8a6a48,#4e6a3c 60%,#2d3f2a)"></div>
      <h3>ANIMAL</h3>
      <a href="#">FIND OUT MORE &#187;</a>
    </div>
    <div class="focus-item" style="left:804px">
      <div class="photo" role="img" aria-label="Family silhouettes holding hands at sunset" style="background:linear-gradient(180deg,#7f8fb4,#e9a066 62%,#2a2a2e 80%)"></div>
      <h3>HUMAN</h3>
      <a href="#">FIND OUT MORE &#187;</a>
    </div>
  </section>

  <section class="feature" style="top:1400px">
    <div class="photo" style="left:0;background:radial-gradient(circle at 25% 15%,#f3f7c4,#6fb04a 40%,#1f5a2e 90%)" role="img" aria-label="Hands holding a glass globe among ferns and moss"></div>
    <div class="copy" style="left:600px;background:var(--panel-mint)">
      <h2>ENVIRONMENT</h2>
      <p>At vero eos et accusamus et iusto odio dignissimos ducimus qui blanditiis praesentium voluptatum deleniti atq ue corr upti quos dolores et quas molestias excepturi sint occaecati cupiditate non provident, similique sunt in culpa qui officia deserunt mollitia animi, id est laborum et dolorum fuga. Et quidem rerum facilis est et expedita distinctio. Nam libero tempore, cum soluta nobis est eligendi...</p>
      <a class="read-more" href="#">READ MORE</a>
    </div>
  </section>

  <section class="feature" style="top:1867px">
    <div class="copy" style="left:0;background:var(--panel-ice)">
      <h2 style="left:125px">ANIMAL</h2>
      <p style="left:128px">At vero eos et accusamus et iusto odio dignissimos ducimus qui blanditiis praesentium voluptatum deleniti atq ue corr upti quos dolores et quas molestias excepturi sint occaecati cupiditate non provident, similique sunt in culpa qui officia deserunt mollitia animi, id est laborum et dolorum fuga. Et quidem rerum facilis est et expedita distinctio. Nam libero tempore, cum soluta nobis est eligendi...</p>
      <a class="read-more" href="#" style="left:131px">READ MORE</a>
    </div>
    <div class="photo" style="left:600px;background:radial-gradient(circle at 55% 30%,#e8503a,#7fa83a 35%,#3d6b28 85%)" role="img" aria-label="Two hummingbirds feeding at a red tropical flower"></div>
  </section>

  <section class="feature" style="top:2334px">
    <div class="photo" style="left:0;background:linear-gradient(180deg,#8f95b6 0%,#f0b08c 45%,#f29a6a 55%,#3a2a26 80%)" role="img" aria-label="Hiker helping another climb a rock at sunset"></div>
    <div class="copy" style="left:600px;background:var(--panel-mint)">
      <h2>HUMAN</h2>
      <p>At vero eos et accusamus et iusto odio dignissimos ducimus qui blanditiis praesentium voluptatum deleniti atq ue corr upti quos dolores et quas molestias excepturi sint occaecati cupiditate non provident, similique sunt in culpa qui officia deserunt mollitia animi, id est laborum et dolorum fuga. Et quidem rerum facilis est et expedita distinctio. Nam libero tempore, cum soluta nobis est eligendi...</p>
      <a class="read-more" href="#">READ MORE</a>
    </div>
  </section>

  <svg class="footer-edge" viewBox="0 0 1200 70" aria-hidden="true">
    <path d="M0 40 C60 30 120 36 200 30 C300 22 400 28 500 24 C600 18 700 22 800 14 C880 8 940 40 1000 44 C1080 48 1140 30 1200 28 L1200 70 L0 70 Z" fill="#4f82ba"/>
  </svg>

  <footer class="site-footer">
    <div class="footer-badge"><div class="name">KELVOR</div></div>

    <div class="footer-col" style="left:477px">
      <h4>GET INVOLVED</h4>
      <a href="#">Join Us</a>
      <a href="#">Fundraise</a>
      <a href="#">Donate</a>
      <a href="#">Shop</a>
    </div>
    <div class="footer-col" style="left:711px">
      <h4>GET HELP</h4>
      <a href="#">Contact Us</a>
      <a href="#">Media</a>
    </div>
    <div class="footer-col" style="left:913px">
      <h4>LEGAL</h4>
      <a href="#">Terms and Conditions</a>
      <a href="#">Cookies</a>
      <a href="#">Privacy Policy</a>
    </div>

    <div class="footer-rule"></div>
    <p class="footer-meta" style="left:112px">CHARITY NUMBER : 000 000 00</p>
    <p class="footer-meta" style="right:111px">2021 Copyrights© Company Name.</p>
  </footer>

</div>
</body>
</html>
```